maple crest homeworks KOVA

Looking for business card design that represents our company. we are maple crest homeworks and we dedicate our skills of home energy efficiency to our customer by providing energy solution to their energy problems.
HVAC
SOLAR
INSULLATION
LIGHTING
DUCT TESTING
KOVA RATING.

```html
<!DOCTYPE html>
<html lang="en">
<head>
<meta charset="utf-8">
<title>Maple Crest Homeworks – Business Cards</title>
<link href="https://fonts.googleapis.com/css2?family=Lato:wght@400;700&family=Arimo:wght@400&display=swap" rel="stylesheet">
<style>
  :root {
    --backdrop: #1f1f1f;
    --card: #141414;
    --card-edge: #262626;
    --silver: #d4d4d4;
    --silver-dim: #a9a9a9;
    --emboss: #2e2e2e;
    --divider: #4a4a4a;
  }
  * { margin: 0; padding: 0; box-sizing: border-box; }
  html, body { width: 1200px; height: 900px; overflow: hidden; }
  body {
    background: var(--backdrop);
    font-family: "Lato", sans-serif;
    position: relative;
  }
  .card {
    position: absolute;
    left: 270px;
    width: 660px;
    height: 377px;
    background: var(--card);
    border: 1px solid var(--card-edge);
    border-radius: 3px;
  }
  .card--front { top: 50px; }
  .card--back { top: 473px; }

  .brand-name {
    font-family: "Lato", sans-serif;
    font-weight: 700;
    text-transform: uppercase;
    line-height: 1.05;
    letter-spacing: 1px;
  }
  .card--front .brand-name {
    position: absolute;
    top: 92px;
    left: 0;
    width: 100%;
    text-align: center;
    font-size: 40px;
    color: var(--silver);
  }
  .services {
    position: absolute;
    top: 248px;
    left: 0;
    width: 100%;
    text-align: center;
    font-family: "Arimo", sans-serif;
    font-size: 15px;
    letter-spacing: 2px;
    line-height: 26px;
    color: var(--silver-dim);
    text-transform: uppercase;
  }

  .card--back .brand-name {
    position: absolute;
    top: 130px;
    left: 34px;
    width: 270px;
    font-size: 32px;
    color: var(--emboss);
  }
  .card--back .divider {
    position: absolute;
    left: 326px;
    top: 70px;
    width: 1px;
    height: 220px;
    background: var(--divider);
  }
  .contact {
    position: absolute;
    left: 350px;
    top: 68px;
    color: var(--silver);
  }
  .contact__name {
    font-size: 27px;
    letter-spacing: 1px;
    font-weight: 400;
  }
  .contact__role {
    font-size: 14px;
    color: var(--silver-dim);
    margin-bottom: 20px;
  }
  .contact__address {
    font-size: 16px;
    line-height: 22px;
    margin-bottom: 8px;
  }
  .contact__line {
    display: flex;
    align-items: center;
    gap: 9px;
    font-size: 16px;
    line-height: 24px;
  }
  .contact__line svg {
    width: 12px;
    height: 12px;
    flex: none;
  }
</style>
</head>
<body>

  <section class="card card--front">
    <div class="brand-name">Maple Crest<br>Homeworks</div>
    <p class="services">
      HVAC - Solar - Insullation<br>
      Lighting - Duct Testing - KOVA Rating.
    </p>
  </section>

  <section class="card card--back">
    <div class="brand-name">Maple Crest<br>Homeworks</div>
    <div class="divider"></div>
    <div class="contact">
      <h1 class="contact__name">DANIEL REYES</h1>
      <p class="contact__role">Director</p>
      <p class="contact__address">214 Alder Lane<br>#02-07B Fairview 480215</p>
      <p class="contact__line">
        <svg viewBox="0 0 12 12" aria-hidden="true"><path d="M2.5 1 L4.5 1 L5.2 3.4 L4 4.3 C4.6 5.8 6.2 7.4 7.7 8 L8.6 6.8 L11 7.5 L11 9.5 C11 10.3 10.3 11 9.5 11 C5 10.7 1.3 7 1 2.5 C1 1.7 1.7 1 2.5 1 Z" fill="var(--silver)"/></svg>
        +330 5817-2493
      </p>
      <p class="contact__line">
        <svg viewBox="0 0 12 12" aria-hidden="true"><rect x="1" y="2.5" width="10" height="7" fill="none" stroke="var(--silver)" stroke-width="1"/><path d="M1 2.5 L6 6.5 L11 2.5" fill="none" stroke="var(--silver)" stroke-width="1"/></svg>
        info@maplecresthomeworks.com
      </p>
      <p class="contact__line">
        <svg viewBox="0 0 12 12" aria-hidden="true"><circle cx="6" cy="6" r="5" fill="none" stroke="var(--silver)" stroke-width="1"/><ellipse cx="6" cy="6" rx="2.2" ry="5" fill="none" stroke="var(--silver)" stroke-width="0.8"/><path d="M1 6 H11" stroke="var(--silver)" stroke-width="0.8"/></svg>
        www.maplecresthomeworks.com
      </p>
    </div>
  </section>

</body>
</html>
```